Online radio: Zintavox homepage redesign

Zintavox is one of the world's leading brands of personalizable online radio -- similar to Kelvessa, but aimed at a somewhat older audience (age 35-54).

We'd like to redesign our homepage with a more contemporary look: It should emphasize our wide variety of GENRES (as the primary navigation), with the search field easy to find as a secondary navigation.

We'd like to retain our corporate color of maroon/plum. (We are not committed to the gold/yellow secondary color.)

See our current homepage at www.zintavox.com and our in-house attempt at an improved design at http://web4.zintavox.com/finder/2013ms/.

Ideally, we'd like to see designs for up to THREE different states:

(1) An initial state when users first come to the page.

(2) What the page would look like as the user is looking at channel options.

(3) What the page would look like once the media player is launched.

However, you may be able to combine (2) and (3) in a single screenshot.

Thanks!

At the request of several designers, we have decided to extend our deadline by four days. At the same time, we have increased our budget, including the addition of a 2nd place award. Thanks for your excellent work!

Reason: Extended at the request of a couple of designers. May mean you don't have to work over the weekend!

Thanks very much for your designs! We are very pleased with the overall quality of the work we are seeing. One reminder: As our brief says, the user interface "should emphasize our wide variety of GENRES (as the primary navigation), with the search field easy to find as a secondary navigation," and we feel that your design uses the SEARCH field as the primary navigation. Many of the designs use a large search field as the primary navigation. If yours does, you might want to tweak your design to put a greater emphasis on browsing genres as the primary navigation. Thanks and good luck!

Target Market(s)

Adults age 35-54 listening to online radio at work

Industry/Entity Type

Radio

Font styles to use
Sans Serif

Requirements
Must have
• This is a design/UI project -- we do not need code

```html
<!DOCTYPE html>
<html lang="en">
<head>
<meta charset="utf-8">
<title>Zintavox – Thousands of Radio Stations</title>
<link rel="stylesheet" href="https://fonts.googleapis.com/css2?family=Jost:wght@400;500;600;700&display=swap">
<style>
:root{
  --plum:#5e1a4c;
  --plum-dark:#4d1340;
  --gold:#ffc414;
  --gold-deep:#f6a800;
  --ink:#4a4a4a;
  --line:#cfcfcf;
  --white:#ffffff;
}
*{margin:0;padding:0;box-sizing:border-box}
html,body{width:1200px;height:906px;overflow:hidden}
body{font-family:"Jost",sans-serif;background:linear-gradient(#ffffff 0,#f7f7f7 60%,#ececec 100%);position:relative;color:var(--ink)}
.topbar{position:absolute;left:0;top:0;width:1200px;height:65px;background:var(--plum);box-shadow:0 3px 8px rgba(0,0,0,.18)}
.brand{position:absolute;left:100px;top:9px;display:flex;align-items:center;gap:8px}
.brand-dot{width:44px;height:44px;border-radius:50%;background:var(--gold)}
.brand-name{color:var(--white);font-size:33px;font-weight:500;letter-spacing:-.5px}
.top-nav{position:absolute;right:99px;top:18px;display:flex;align-items:center;height:28px}
.top-nav .item{color:var(--white);font-size:15px;font-weight:600;padding:0 12px;border-left:1px solid rgba(255,255,255,.45);line-height:18px;display:flex;align-items:center}
.top-nav .item:first-child{border-left:0}
.top-nav .item:last-child{padding-right:0}
.headline{position:absolute;left:0;width:1200px;top:128px;text-align:center;color:var(--plum);font-size:33px;line-height:38px;font-weight:400}
.headline strong{font-weight:700}
.search{position:absolute;left:292px;top:230px;width:605px;height:57px;border:1px solid #c8c8c8;border-radius:3px;background:var(--white);box-shadow:inset 0 1px 3px rgba(0,0,0,.08)}
.search-field{position:absolute;left:11px;top:16px;font-size:19px;color:#a8a8a8}
.search-btn{position:absolute;right:-1px;top:-1px;width:72px;height:57px;background:var(--plum);border-radius:0 3px 3px 0;display:flex;align-items:center;justify-content:center}
.search-hint{position:absolute;left:0;width:1168px;top:299px;text-align:center;font-size:16px;color:#555}
.tabs{position:absolute;left:118px;top:389px;display:flex;gap:16px}
.tab{width:182px;height:44px;border-radius:8px 8px 0 0;background:linear-gradient(var(--gold),var(--gold-deep));color:var(--plum);font-weight:700;font-size:16px;text-align:center;line-height:44px}
.tab.is-active{background:var(--plum);color:var(--white);margin-left:-4px;margin-right:-4px;width:182px}
.panel{position:absolute;left:101px;top:433px;width:999px;height:330px;background:var(--white);border:1px solid var(--line);box-shadow:0 4px 8px rgba(0,0,0,.08)}
.panel-title{position:absolute;left:104px;top:22px;width:762px;text-align:center;font-size:17px;font-weight:700;color:var(--plum)}
.panel-title::before,.panel-title::after{content:"";position:absolute;top:11px;width:248px;height:1px;background:#d8d8d8}
.panel-title::before{left:0}.panel-title::after{right:0}
.channel{position:absolute;top:66px;width:190px;text-align:center}
.channel-art{display:block;margin:0 auto;width:168px;height:110px;border:2px solid #444;box-shadow:0 1px 3px rgba(0,0,0,.3)}
.channel-name{margin-top:8px;font-size:15px;font-weight:700;color:var(--plum);line-height:18px}
.channel-desc{font-size:14px;line-height:19px;color:#555}
.play{display:inline-flex;align-items:center;gap:6px;margin-top:6px;height:24px;padding:0 10px 0 4px;border:2px solid var(--plum);border-radius:13px;background:var(--plum);color:var(--gold);font-weight:700;font-size:14px}
.play-icon{width:16px;height:16px;border-radius:50%;background:var(--white);display:flex;align-items:center;justify-content:center}
.scroll-track{position:absolute;left:9px;top:304px;width:982px;height:1px;background:#999}
.scroll-thumb{position:absolute;left:25px;top:299px;width:67px;height:12px;background:var(--gold)}
.genre-links{position:absolute;top:803px;left:0;width:1200px;font-size:16px;font-weight:700;color:var(--plum)}
.genre-links span{position:absolute}
.footer{position:absolute;left:0;top:857px;width:1200px;height:49px;background:var(--plum)}
.footer-links{position:absolute;left:100px;top:19px;display:flex;gap:22px;color:var(--white);font-size:12px;font-weight:500}
.social{position:absolute;right:121px;top:14px;display:flex;gap:9px}
.social span{width:26px;height:26px;border-radius:50%;background:var(--white)}
</style>
</head>
<body>
<header class="topbar">
  <div class="brand"><span class="brand-dot"></span><span class="brand-name">Zintavox</span></div>
  <nav class="top-nav">
    <span class="item" aria-label="Random station">
      <svg width="24" height="24" viewBox="0 0 24 24"><rect x="2" y="2" width="20" height="20" rx="5" fill="#e8e0e6"/><circle cx="7.5" cy="7.5" r="2" fill="#5e1a4c"/><circle cx="16.5" cy="7.5" r="2" fill="#5e1a4c"/><circle cx="12" cy="12" r="2" fill="#5e1a4c"/><circle cx="7.5" cy="16.5" r="2" fill="#5e1a4c"/><circle cx="16.5" cy="16.5" r="2" fill="#5e1a4c"/></svg>
    </span>
    <span class="item" aria-label="Help">
      <svg width="24" height="24" viewBox="0 0 24 24"><circle cx="12" cy="12" r="11" fill="#fff"/><path d="M8.6 9.3a3.4 3.4 0 1 1 4.7 3.1c-.9.4-1.3 1-1.3 2v.6" stroke="#5e1a4c" stroke-width="2.4" fill="none" stroke-linecap="round"/><circle cx="12" cy="18.3" r="1.4" fill="#5e1a4c"/></svg>
    </span>
    <span class="item">LOG IN</span>
    <span class="item">JOIN FOR FREE</span>
  </nav>
</header>

<h1 class="headline">THOUSANDS OF<br><strong>RADIO STATIONS</strong> WITH ENDLESS MUSIC</h1>

<div class="search">
  <span class="search-field">Find the radio that plays your favorite music</span>
  <span class="search-btn">
    <svg width="26" height="26" viewBox="0 0 26 26"><circle cx="11" cy="11" r="7.5" stroke="#fff" stroke-width="3.5" fill="none"/><path d="M16.5 16.5l6 6" stroke="#fff" stroke-width="4.5" stroke-linecap="round"/></svg>
  </span>
</div>
<p class="search-hint">For Example : Search by Artist or Keyword etc</p>

<nav class="tabs">
  <span class="tab">MY HISTORY</span>
  <span class="tab">MY FAVORITE</span>
  <span class="tab is-active">MOST POPULAR</span>
  <span class="tab">WORKDAY MOODS</span>
  <span class="tab">GENRES</span>
</nav>

<section class="panel">
  <h2 class="panel-title">MOST POPULAR CHANNELS</h2>

  <article class="channel" style="left:-1px">
    <span class="channel-art" role="img" aria-label="Artist photo for channel" style="background:linear-gradient(135deg,#3b2a22,#c9a78d 55%,#6b5245)"></span>
    <div class="channel-name">Magic Sunny Lite Mix</div>
    <div class="channel-desc">Today's best adult hit music,<br>some softer...</div>
    <span class="play"><span class="play-icon"><svg width="8" height="9" viewBox="0 0 8 9"><path d="M1 0l7 4.5L1 9z" fill="#5e1a4c"/></svg></span>PLAY</span>
  </article>
  <article class="channel" style="left:203px">
    <span class="channel-art" role="img" aria-label="Artist photo for channel" style="background:linear-gradient(135deg,#0e1f5c,#2d4bb0 50%,#1a1230)"></span>
    <div class="channel-name">Magic Sunny Lite Mix</div>
    <div class="channel-desc">Today's best adult hit music,<br>some softer...</div>
    <span class="play"><span class="play-icon"><svg width="8" height="9" viewBox="0 0 8 9"><path d="M1 0l7 4.5L1 9z" fill="#5e1a4c"/></svg></span>PLAY</span>
  </article>
  <article class="channel" style="left:405px">
    <span class="channel-art" role="img" aria-label="Artist photo for channel" style="background:linear-gradient(135deg,#2a2a2a,#6e6a60 50%,#c7c6b5)"></span>
    <div class="channel-name">Magic Sunny Lite Mix</div>
    <div class="channel-desc">Today's best adult hit music,<br>some softer...</div>
    <span class="play"><span class="play-icon"><svg width="8" height="9" viewBox="0 0 8 9"><path d="M1 0l7 4.5L1 9z" fill="#5e1a4c"/></svg></span>PLAY</span>
  </article>
  <article class="channel" style="left:607px">
    <span class="channel-art" role="img" aria-label="Artist photo for channel" style="background:linear-gradient(135deg,#e9eef6,#8a9bb3 55%,#d9e2ee)"></span>
    <div class="channel-name">Magic Sunny Lite Mix</div>
    <div class="channel-desc">Today's best adult hit music,<br>some softer...</div>
    <span class="play"><span class="play-icon"><svg width="8" height="9" viewBox="0 0 8 9"><path d="M1 0l7 4.5L1 9z" fill="#5e1a4c"/></svg></span>PLAY</span>
  </article>
  <article class="channel" style="left:810px">
    <span class="channel-art" role="img" aria-label="Artist photo for channel" style="background:linear-gradient(135deg,#3a0d0d,#8a2a1e 50%,#1a1a2a)"></span>
    <div class="channel-name">Magic Sunny Lite Mix</div>
    <div class="channel-desc">Today's best adult hit music,<br>some softer...</div>
    <span class="play"><span class="play-icon"><svg width="8" height="9" viewBox="0 0 8 9"><path d="M1 0l7 4.5L1 9z" fill="#5e1a4c"/></svg></span>PLAY</span>
  </article>

  <span class="scroll-track"></span>
  <span class="scroll-thumb"></span>
</section>

<nav class="genre-links">
  <span style="left:135px">TOP 40 / POP HITS</span>
  <span style="left:340px">LITE HITS</span>
  <span style="left:478px">COUNTRY</span>
  <span style="left:609px">CLASSICAL</span>
  <span style="left:758px">CLASSIC ROCK</span>
  <span style="left:935px">SMOOTH JAZZ</span>
</nav>

<footer class="footer">
  <nav class="footer-links"><span>HELP</span><span>ABOUT &amp; CONTACT</span><span>MOBILE</span></nav>
  <div class="social" aria-label="Social links"><span></span><span></span><span></span><span></span></div>
</footer>
</body>
</html>
```